Career Counsellor Training Course

Corvent Staffing Partners is an executive coaching and outplacement business in Australia that needs a 1-page flyer made to publicise our career counselling courses. We are organisational psychologists and experienced career coaches who work for companies that are downsizing. This flyer seeks to publicise our expertise and CREDIBILITY in training new consultants as career coaches. I have attached a previous design that outlines our services to our organisational customers. The audience for THIS flyer is psychologists and consultants who want training to deliver our programs. The final design should reflect a professional business personality and use the same colours as our business. We will supply the CMYK codes however the attached flyer should provide a starting point. In our last project we learned that we will need 2mm bleed for printing. We are looking for a really impactful design using my photo as the centrepiece and for professional, credible font and desktop design to deliver a friendly professional image for our brand.
Target Market(s)
Psychologists and consultants who want to get professional training in career counselling.
Industry/Entity Type
Business
Requirements
Must have
- Visual impact that is highly professional.
Nice to have
- Our logo and name are important to us. This is an opportunity for a designer to add a "brand personality" that is based around our own photography + our logo + "credibility" as the theme.

```html
<!DOCTYPE html>
<html lang="en">
<head>
<meta charset="utf-8">
<title>Corvent Staffing Partners – Outplacement Service Flyer</title>
<link href="https://fonts.googleapis.com/css2?family=Oswald:wght@500;600;700&family=Lato:wght@400;700&display=swap" rel="stylesheet">
<style>
  :root{
    --navy:#0b3f8c;
    --brand:#0f5cad;
    --sky:#5a9bd4;
    --sky-light:#b9d4ee;
    --ink:#333a44;
    --grey:#50545a;
    --white:#ffffff;
    --paper:#fbfbfb;
  }
  *{margin:0;padding:0;box-sizing:border-box}
  html,body{width:900px;height:1200px;overflow:hidden;background:var(--white)}
  .flyer{position:relative;width:900px;height:1200px;background:var(--paper);font-family:"Lato",Arial,sans-serif;color:var(--ink);overflow:hidden}
  .layer{position:absolute;left:0;top:0}
  .brand-mark{position:absolute;left:34px;top:278px;display:flex;align-items:center;gap:10px}
  .brand-mark__square{width:16px;height:16px;background:var(--brand)}
  .brand-mark__name{font-family:"Lato",Arial,sans-serif;font-weight:700;font-size:30px;letter-spacing:2px;color:var(--brand)}
  .about{position:absolute;left:0;top:434px;width:311px}
  .about__tab{position:absolute;left:0;top:96px;width:228px;height:52px;background:var(--white);border-radius:0 8px 8px 0;box-shadow:2px 3px 4px rgba(0,0,0,.25);display:flex;align-items:center;padding-left:46px}
  .about__tab h2{font-family:"Oswald",Arial,sans-serif;font-weight:700;font-size:32px;color:var(--brand);letter-spacing:.5px}
  .about__text{position:absolute;left:40px;top:168px;width:264px;color:var(--white);font-size:16.5px;line-height:1.3;text-align:justify}
  .about__text p+p{margin-top:16px}
  .portrait{position:absolute;left:0;top:855px;width:324px;height:281px}
  .offer{position:absolute;left:350px;top:526px;width:530px}
  .offer__title{font-family:"Oswald",Arial,sans-serif;font-weight:600;color:var(--brand);font-size:88px;line-height:1;letter-spacing:1px}
  .offer__subtitle{font-family:"Oswald",Arial,sans-serif;font-weight:600;color:var(--grey);font-size:44px;line-height:1.1;margin-top:2px}
  .section-head{font-family:"Oswald",Arial,sans-serif;font-weight:700;color:var(--brand);font-size:35px;line-height:1}
  .learn{position:absolute;left:352px;top:692px;width:520px}
  .learn ul{list-style:none;margin-top:12px;font-size:15.5px;line-height:1.3}
  .learn li::before{content:"• "}
  .work{position:absolute;left:355px;top:845px;width:520px}
  .work p{font-size:15.5px;line-height:1.27;margin-top:14px}
  .work p+p{margin-top:20px}
  .footer{position:absolute;left:0;top:1136px;width:900px;height:64px;background:var(--brand);display:flex;align-items:center;color:var(--white)}
  .footer__call{width:325px;text-align:center;font-weight:700;font-size:27px}
  .footer__web{margin-left:50px;font-size:26px;letter-spacing:4.5px}
</style>
</head>
<body>
<main class="flyer">
  <svg class="layer hero-photo" width="900" height="1200" viewBox="0 0 900 1200" role="img" aria-label="Photo of a businessman in a dark suit holding a glowing work–life balance sphere between his hands">
    <defs>
      <radialGradient id="heroTone" cx="0.62" cy="0.4" r="0.7">
        <stop offset="0" stop-color="#4c6e96"/>
        <stop offset="0.5" stop-color="#213a5c"/>
        <stop offset="1" stop-color="#0f1f36"/>
      </radialGradient>
    </defs>
    <polygon points="0,0 900,0 900,555 311,370" fill="url(#heroTone)"/>
  </svg>

  <svg class="layer frame" width="900" height="1200" viewBox="0 0 900 1200" aria-hidden="true">
    <polygon points="0,0 311,370 0,434" fill="var(--white)"/>
    <polygon points="0,460 311,396 311,1136 0,1136" fill="var(--sky)"/>
    <polygon points="0,0 22,0 322,357 311,370" fill="var(--white)"/>
    <polyline points="6,0 318,372" stroke="var(--sky)" stroke-width="4" fill="none"/>
    <polyline points="26,0 334,366" stroke="var(--brand)" stroke-width="6" fill="none"/>
    <polygon points="0,434 311,370 900,555 900,576 311,392 0,458" fill="var(--white)"/>
    <polyline points="0,444 311,380 900,565" stroke="var(--brand)" stroke-width="9" fill="none"/>
    <polyline points="311,392 900,577" stroke="var(--sky-light)" stroke-width="7" fill="none"/>
  </svg>

  <div class="brand-mark">
    <span class="brand-mark__square"></span>
    <span class="brand-mark__name">CORVENT</span>
  </div>

  <section class="about">
    <div class="about__tab"><h2>ABOUT US</h2></div>
    <div class="about__text">
      <p>Corvent Staffing Partners is a talent management, outplacement and leadership development consultancy dedicated to developing your career and organisational success.</p>
      <p>Our qualified organisational psychologists conduct training for new career coaches and master classes for experienced practitioners.</p>
    </div>
  </section>

  <svg class="portrait" width="324" height="281" viewBox="0 0 324 281" role="img" aria-label="Portrait photo of the lead consultant in a dark blazer and light blue shirt">
    <defs>
      <linearGradient id="portraitTone" x1="0" y1="0" x2="0" y2="1">
        <stop offset="0" stop-color="#f2f2f2"/>
        <stop offset="0.55" stop-color="#c9b6a4"/>
        <stop offset="1" stop-color="#1e2430"/>
      </linearGradient>
    </defs>
    <rect width="324" height="281" fill="url(#portraitTone)"/>
  </svg>

  <header class="offer">
    <h1 class="offer__title">THE BEST</h1>
    <p class="offer__subtitle">OUT PLACEMENT SERVICE</p>
  </header>

  <section class="learn">
    <h2 class="section-head">YOU WILL LEARN</h2>
    <ul>
      <li>evidence-based coaching skills</li>
      <li>how to use validated career assessment tools</li>
      <li>how to support organisations that are going though change</li>
    </ul>
  </section>

  <section class="work">
    <h2 class="section-head">WORK WITH US</h2>
    <p>Our customers are human resource professionals, line managers and senior executives who are responsible for managing people in organisations. Our customers seek our assistance when they are facing a period of uncertainty, a major change, or have identified that one of their people requires external coaching support.</p>
    <p>At Corvent, we are known for the expertise of our consultants across assessment and development of leadership capability and providing personalised outplacement and career transition support to employees and teams that are undergoing change. We look forward to exploring your talent needs and how our team of expert, qualified coaches can make a difference.</p>
  </section>

  <footer class="footer">
    <span class="footer__call">CALL 1800 CORVENT</span>
    <span class="footer__web">www.corventsp.com.au</span>
  </footer>
</main>
</body>
</html>
```